Business card and Stationery for data intelligence company

We need a new design for our business cards and stationery (Business Letter templates and a Quote example on Word, but it MUST work on Google Doc as well).

We are a software company based in Ireland and UK. Our product is "Quarla", data intelligence platform with beautiful visualizations, graph capabilities (things are interconnected), powerful, flexible, it can manage Big Data and Streaming information. It's modern and relatively open source.
Our company will provide data intelligence for law enforcements, pharmaceuticals, and similar high end customers.

We'll launch a new website soon. At the moment it's http://www.quarla.tech if you want to take a look. This is our youtube channel in case you need it to understand what Quarla is: https://www.youtube.com/c/quarlatechchannel

We changed the logo so please use the logo I attach here.

We'd like the output to be cool and modern but elegant and "business" at the same time. It should inspire simple sophistication, "unity" "intent" "purpose" yet subtly very advanced and innovative.

The name "Quarla" does NOT refer to sirens (mithological creatures) as well as the warning devices. It means Quantum Unified Archival Record Layer Array. Please use our logo's colors and if you want to something like the "graph" image.

```html
<!DOCTYPE html>
<html lang="en">
<head>
<meta charset="utf-8">
<title>Quarla Business Card</title>
<link href="https://fonts.googleapis.com/css2?family=Open+Sans:wght@400;600&display=swap" rel="stylesheet">
<style>
  :root {
    --stage: #1f1f1f;
    --orange: #fbb03b;
    --grey: #b3b3b3;
    --panel-light: #ffffff;
    --panel-soft: #ececec;
    --white: #ffffff;
  }
  * { margin: 0; padding: 0; box-sizing: border-box; }
  html, body {
    width: 1200px;
    height: 987px;
    overflow: hidden;
    background: var(--stage);
    font-family: "Open Sans", Arial, sans-serif;
  }
  .card {
    position: absolute;
    width: 615px;
    height: 351px;
    overflow: hidden;
  }
  .card-front { left: 293px; top: 130px; background: var(--orange); }
  .card-back  { left: 293px; top: 505px; background: var(--grey); }

  .brand-panel {
    position: absolute;
    left: 262px;
    top: 0;
    width: 353px;
    height: 351px;
    background: linear-gradient(135deg, var(--panel-light) 0%, var(--panel-light) 55%, var(--panel-soft) 100%);
  }

  .contact-block {
    position: absolute;
    left: 32px;
    top: 58px;
    color: var(--white);
  }
  .person-name { font-size: 20px; font-weight: 600; letter-spacing: 0.3px; line-height: 1.2; }
  .person-role { font-size: 16px; font-weight: 400; line-height: 1.3; }
  .address { margin-top: 15px; font-size: 15px; line-height: 22px; }
  .contact-list { list-style: none; margin-top: 9px; font-size: 15px; }
  .contact-list li { display: flex; align-items: center; height: 23.4px; }
  .contact-list svg { width: 16px; height: 16px; margin-right: 13px; fill: var(--white); flex: none; }

  .brand {
    position: absolute;
    display: flex;
    align-items: center;
  }
  .brand-front { left: 320px; top: 142px; }
  .brand-mark { border-radius: 50%; flex: none; }
  .brand-front .brand-mark { width: 56px; height: 56px; border: 8px solid var(--orange); margin-right: 20px; }
  .brand-name { font-weight: 600; letter-spacing: 3px; }
  .brand-front .brand-name { color: var(--orange); font-size: 30px; }

  .brand-back { left: 0; right: 0; top: 0; bottom: 0; justify-content: center; }
  .brand-back .brand-mark { width: 117px; height: 117px; border: 16px solid var(--white); margin-right: 24px; }
  .brand-back .brand-name { color: var(--white); font-size: 56px; letter-spacing: 6px; }
</style>
</head>
<body>

<section class="card card-front">
  <div class="brand-panel" role="img" aria-label="Decorative ring graphic area in white, orange and grey"></div>

  <div class="contact-block">
    <p class="person-name">MAREK OLIN</p>
    <p class="person-role">President</p>
    <p class="address">2716 Harrowgate Lane<br>Cedar Bay, NY 11904</p>
    <ul class="contact-list">
      <li><svg viewBox="0 0 16 16"><path d="M2 5c0-2 2-3 6-3s6 1 6 3v1h-3V5H5v1H2z"/><path d="M4 7h8l2 6H2z"/><circle cx="8" cy="10" r="1.6" fill="var(--orange)"/></svg>514 2908 7731</li>
      <li><svg viewBox="0 0 16 16"><path d="M4.5 1h7a1 1 0 0 1 1 1v12a1 1 0 0 1-1 1h-7a1 1 0 0 1-1-1V2a1 1 0 0 1 1-1zm.5 2v9h6V3z"/></svg>842 6190 3357</li>
      <li><svg viewBox="0 0 16 16"><path d="M4 1h8v4H4z"/><path d="M1 6h14v6h-2v-2H3v2H1z"/><path d="M4 11h8v4H4z"/></svg>836 5071 2448</li>
      <li><svg viewBox="0 0 16 16"><path d="M1 4h14v1L8 9 1 5z"/><path d="M1 6.5l7 4 7-4V13H1z"/></svg>marek@quarla.tech</li>
      <li><svg viewBox="0 0 16 16"><circle cx="8" cy="8" r="7"/><path d="M5 4c1 1 2 1 2 3s-2 1-2 3 1 3 1 3M10 3c0 2 2 2 3 3M9 9c1 0 2 1 2 3" stroke="var(--orange)" stroke-width="1.3" fill="none"/></svg>www.quarla.tech</li>
    </ul>
  </div>

  <div class="brand brand-front">
    <span class="brand-mark"></span>
    <span class="brand-name">QUARLA</span>
  </div>
</section>

<section class="card card-back">
  <div class="brand brand-back">
    <span class="brand-mark"></span>
    <span class="brand-name">QUARLA</span>
  </div>
</section>

</body>
</html>
```